Nonprofit Women's Association Website

We are a nonprofit women's association based in our village, dedicated to making a positive impact on our community. Our organization actively participates in village events, organizes activities for our female members, including courses and excursions and provides financial support to various social organizations. We are also responsible for running a meal delivery service for elderly individuals in need and organizing a children's clothing exchange event.
We are looking for a webdesign that features:
- user friendly design, welcoming, women centered
- showcase our activities (courses in knitting, handcrafting, etc.), outings, excursions, meal delivery service, children's cloth exchange, etc.
- highlight social impact
- highlight female members (maybe faces)
Design Elements:
- logo (see attachment), it's not that nice, but it's a requirement to use this logo
- we are open to your creative suggestions for the design of the website, including color schemes, imagery and layout
- the website will be implemented using wordpress, any template proposals are highly appreciated

```html
<!DOCTYPE html>
<html lang="en">
<head>
<meta charset="utf-8">
<title>Nonprofit Women's Association</title>
<link href="https://fonts.googleapis.com/css2?family=Montserrat:wght@400;500;600;700&family=Oswald:wght@400;500&display=swap" rel="stylesheet">
<style>
:root{
  --rose:#e0305a;
  --rose-soft:#dc4168;
  --ink:#231f20;
  --charcoal:#3a3435;
  --mist:#f7f7f7;
  --line:#d8d8d8;
  --white:#ffffff;
}
*{box-sizing:border-box;margin:0;padding:0}
html,body{width:1200px;height:4303px;overflow:hidden}
body{position:relative;font-family:'Montserrat',sans-serif;color:var(--ink);background:var(--white)}
.abs{position:absolute}
section,header,footer{position:absolute;left:0;width:1200px}

/* header */
.site-header{top:0;height:114px;background:var(--white);border-bottom:1px solid var(--line)}
.brand{left:122px;top:14px;display:flex;align-items:center;gap:10px;font-weight:700;font-size:22px;color:var(--ink)}
.brand-dot{width:26px;height:26px;border-radius:50%;background:var(--rose)}
.follow{right:112px;top:20px;display:flex;align-items:center;gap:8px;font-size:15px;color:#666}
.follow i{display:block;width:16px;height:16px;border-radius:50%;background:var(--charcoal)}
.follow i:first-of-type{background:#3b6fd8}
.follow i:nth-of-type(2){background:var(--rose)}
.nav-rule{left:0;top:60px;width:1200px;height:1px;background:var(--line)}
.main-nav{left:122px;top:60px;height:54px;display:flex;font-size:14.5px}
.main-nav a{display:flex;align-items:center;padding:0 11px;margin-right:7px;color:var(--ink);text-decoration:none}
.main-nav a.active{background:var(--rose);color:var(--white)}

/* hero */
.hero{top:114px;height:526px;background:linear-gradient(100deg,#2e2826 0%,#5d534f 45%,#a89a92 75%,#c9bdb5 100%)}
.hero-title{left:122px;top:100px;font-family:'Oswald',sans-serif;font-weight:400;font-size:58px;line-height:60px;color:var(--white)}
.hero-text{left:122px;top:236px;width:478px;font-size:19px;line-height:25px;color:var(--white)}
.btn{display:inline-flex;align-items:center;justify-content:center;background:var(--rose);color:var(--white);text-decoration:none}
.hero-btn{left:122px;top:327px;width:155px;height:44px;font-family:'Oswald',sans-serif;font-size:21px}
.dots{left:561px;top:472px;display:flex;gap:5px}
.dots span{width:12px;height:12px;border-radius:50%;border:1.5px solid var(--white)}
.dots span.on{background:var(--rose);border-color:var(--rose)}

/* headings */
.section-title{width:1200px;left:0;text-align:center;font-weight:600;font-size:36px}
.divider{left:516px;width:168px;height:24px}

/* about */
.about{top:640px;height:994px;background:var(--mist)}
.member{top:174px;width:162px;height:174px}
.member.active{outline:5px solid var(--rose);outline-offset:0}
.member-pointer{left:965px;top:352px;width:0;height:0;border-left:14px solid transparent;border-right:14px solid transparent;border-top:12px solid var(--rose)}
.profile-name{left:125px;top:446px;font-size:33px;font-weight:500;letter-spacing:.5px}
.profile-name span{color:var(--rose)}
.profile-text{left:122px;top:506px;width:394px;font-size:18.5px;line-height:28.5px;text-align:justify}
.profile-text p+p{margin-top:14px}
.profile-social{left:122px;top:736px;display:flex;gap:16px}
.profile-social i{display:block;width:16px;height:16px;border-radius:50%;background:var(--ink)}
.profile-frame{left:729px;top:421px;width:324px;height:438px;background:var(--rose)}
.profile-photo{left:578px;top:438px;width:458px;height:459px}

/* what we do */
.what{top:1634px;height:542px;background:var(--mist)}
.what-band{left:0;top:0;width:1200px;height:318px;background:linear-gradient(180deg,#3b2f31,#2a2223)}
.what .section-title{top:48px;color:var(--white)}
.service{top:127px;width:222px;height:415px;background:var(--white);box-shadow:0 2px 6px rgba(0,0,0,.18);text-align:center}
.service-img{position:absolute;left:8px;top:10px;width:206px;height:161px}
.service h3{position:absolute;left:0;top:192px;width:100%;font-size:15.5px;font-weight:600}
.service p{position:absolute;left:18px;top:221px;width:186px;font-size:13.5px;line-height:21px;color:#444}
.service .btn{position:absolute;left:50px;top:321px;width:122px;height:39px;font-size:14px;font-weight:500}

/* how */
.how{top:2176px;height:514px;background:var(--mist)}
.how .section-title{top:70px;color:var(--rose)}
.step{width:200px;text-align:center;font-size:20px;line-height:24px;color:#333}
.step-icon{width:136px;height:136px;border-radius:50%;background:var(--charcoal)}
.step-icon.hot{background:var(--rose)}

/* activities */
.activities{top:2690px;height:716px;background:linear-gradient(135deg,#dc3a63,#d54870 60%,#df3a60)}
.activities .section-title{top:84px;color:var(--white)}
.activity{top:187px;width:408px;height:403px;background:var(--white);border-radius:0 0 14px 14px;overflow:hidden;text-align:center}
.activity-img{position:absolute;left:0;top:0;width:408px;height:206px}
.activity h3{position:absolute;left:0;top:236px;width:100%;font-size:24px;font-weight:700}
.activity p{position:absolute;left:36px;top:282px;width:336px;font-size:15px;line-height:21.5px;color:#333}

/* testimonials */
.voices{top:3406px;height:559px;background:var(--white)}
.voices-title{left:122px;top:124px;font-size:30px;font-weight:500;line-height:38px}
.voices-title span{color:var(--rose)}
.voices-img{left:662px;top:86px;width:421px;height:335px}
.arrow{top:196px;width:34px;height:34px}
.quote-card{left:272px;top:245px;width:440px;height:239px;background:var(--white);box-shadow:0 2px 10px rgba(0,0,0,.2)}
.quote-card p{position:absolute;left:40px;top:34px;width:360px;font-size:20px;line-height:27px;color:#444}
.stars{position:absolute;left:40px;top:178px;color:var(--rose);font-size:17px;letter-spacing:3px}
.quote-name{position:absolute;left:244px;top:181px;color:var(--rose);font-size:16px}
.avatar{position:absolute;left:337px;top:153px;width:78px;height:78px;border-radius:50%;background:#dfe6ee}

/* footer */
.site-footer{top:3965px;height:338px;background:var(--charcoal);color:var(--white)}
.footer-title{left:0;top:68px;width:1200px;text-align:center;font-size:34px;font-weight:500}
.footer-rule{left:122px;width:964px;height:1px;background:#8a8485}
.footer-nav{left:122px;top:151px;width:964px;display:flex;justify-content:space-around;font-size:14px;padding:0 40px}
.footer-nav a{color:var(--white);text-decoration:none}
.copyright{left:0;top:252px;width:1200px;text-align:center;font-size:14px}
</style>
</head>
<body>

<header class="site-header">
  <div class="abs brand"><span class="brand-dot"></span>Women's Circle</div>
  <div class="abs follow">Follow us: <i></i><i></i><i></i></div>
  <div class="abs nav-rule"></div>
  <nav class="abs main-nav">
    <a class="active">Home</a><a>About us</a><a>Our Activities</a><a>Our Services</a><a>Members Area</a><a>How We Do It?</a><a>Testimonials</a><a>Contact us</a>
  </nav>
</header>

<section class="hero" role="img" aria-label="Photo of two women talking, one gesturing with her hands">
  <h1 class="abs hero-title">EMPOWERING PEOPLE<br>WHO HELP PEOPLE</h1>
  <p class="abs hero-text">Lorem Ipsum is simply dummy text of the printing and typesetting industry. Lorem Ipsum has been the industry's</p>
  <a class="abs btn hero-btn">READ MORE</a>
  <div class="abs dots"><span></span><span></span><span class="on"></span><span></span><span></span></div>
</section>

<section class="about">
  <h2 class="abs section-title" style="top:62px">ABOUT US</h2>
  <svg class="abs divider" style="top:108px" viewBox="0 0 168 24"><line x1="0" y1="12" x2="58" y2="12" stroke="#333"/><line x1="110" y1="12" x2="168" y2="12" stroke="#333"/><path d="M62 20h44a22 14 0 0 0-44 0z" fill="#3a3435"/></svg>
  <div class="abs member" style="left:140px;background:linear-gradient(#6b5a4f,#c9b7a8)" role="img" aria-label="Portrait of a member"></div>
  <div class="abs member" style="left:329px;background:linear-gradient(#1c1a1a,#5a4540)" role="img" aria-label="Portrait of a member"></div>
  <div class="abs member" style="left:520px;background:linear-gradient(#4d6a3e,#c77b72)" role="img" aria-label="Portrait of a member"></div>
  <div class="abs member" style="left:710px;background:linear-gradient(#c6c3bd,#6f6a66)" role="img" aria-label="Portrait of a member"></div>
  <div class="abs member active" style="left:899px;background:linear-gradient(#9fb1c2,#8a7d78)" role="img" aria-label="Portrait of Maren Holt"></div>
  <div class="abs member-pointer"></div>
  <h3 class="abs profile-name">MAREN <span>HOLT</span></h3>
  <div class="abs profile-text">
    <p>Lorem Ipsum is simply dummy text of the printing and typesetting industry.</p>
    <p>Lorem Ipsum has been the industry's standard dummy text ever since the 1500s, when an unknown printer took a galley of type and scrambled it to make a type specimen book.</p>
  </div>
  <div class="abs profile-social"><i></i><i></i><i></i></div>
  <div class="abs profile-frame"></div>
  <div class="abs profile-photo" style="background:linear-gradient(160deg,#b9c8d6,#8d8a88 70%,#5d5350)" role="img" aria-label="Portrait of Maren Holt in a light jacket"></div>
</section>

<section class="what">
  <div class="abs what-band"></div>
  <h2 class="abs section-title">WHAT WE DO</h2>
  <article class="abs service" style="left:122px"><div class="service-img" style="background:linear-gradient(#6f8a52,#8a7a5a)" role="img" aria-label="Child walking on logs in a forest"></div><h3>OUTINGS</h3><p>Lorem Ipsum is simply dummy text of the printing and typesetting industry.</p><a class="btn">READ MORE</a></article>
  <article class="abs service" style="left:368px"><div class="service-img" style="background:linear-gradient(#8aa45e,#3c5678)" role="img" aria-label="Group of people hiking in the woods"></div><h3>EXCRUSIONS</h3><p>Lorem Ipsum is simply dummy text of the printing and typesetting industry.</p><a class="btn">READ MORE</a></article>
  <article class="abs service" style="left:613px"><div class="service-img" style="background:linear-gradient(#dcdcd8,#c9a27a)" role="img" aria-label="Children sharing a meal at a table"></div><h3>MEAL DELIVERY</h3><p>Lorem Ipsum is simply dummy text of the printing and typesetting industry.</p><a class="btn">READ MORE</a></article>
  <article class="abs service" style="left:866px"><div class="service-img" style="background:linear-gradient(#b7b0a3,#a14a4a 60%,#6d6a5e)" role="img" aria-label="Children's clothes hanging on a line"></div><h3>CLOTH EXCHANGE</h3><p>Lorem Ipsum is simply dummy text of the printing and typesetting industry.</p><a class="btn">READ MORE</a></article>
</section>

<section class="how">
  <h2 class="abs section-title">HOW WE DO IT</h2>
  <svg class="abs divider" style="top:122px" viewBox="0 0 168 24"><line x1="0" y1="12" x2="58" y2="12" stroke="#333"/><line x1="110" y1="12" x2="168" y2="12" stroke="#333"/><path d="M62 20h44a22 14 0 0 0-44 0z" fill="#3a3435"/></svg>
  <svg class="abs" style="left:270px;top:190px" width="680" height="90" viewBox="0 0 680 90" fill="none" stroke="#444" stroke-width="1.5" stroke-dasharray="3 4">
    <path d="M5 70 C80 95 130 70 170 30 S240 5 258 18"/><path d="M252 12l6 6-8 2" stroke-dasharray="none"/>
    <path d="M405 25 C450 -5 500 10 540 50 S620 80 655 60"/><path d="M648 56l7 4-6 5" stroke-dasharray="none"/>
  </svg>
  <div class="abs step-icon" style="left:122px;top:187px"></div>
  <div class="abs step-icon hot" style="left:532px;top:187px"></div>
  <div class="abs step-icon" style="left:948px;top:187px"></div>
  <svg class="abs" style="left:964px;top:203px" width="104" height="104" viewBox="0 0 104 104"><circle cx="52" cy="52" r="28" fill="none" stroke="#fff" stroke-width="9"/><circle cx="52" cy="52" r="11" fill="none" stroke="#fff" stroke-width="6"/></svg>
  <p class="abs step" style="left:90px;top:334px">Lorem Ipsum is simply dummy text of the printing and typesetting industry.</p>
  <p class="abs step" style="left:500px;top:338px">Lorem Ipsum is simply dummy text of the printing and typesetting industry.</p>
  <p class="abs step" style="left:916px;top:338px">Lorem Ipsum is simply dummy text of the printing and typesetting industry.</p>
</section>

<section class="activities">
  <h2 class="abs section-title">OUR ACTIVITIES</h2>
  <article class="abs activity" style="left:122px"><div class="activity-img" style="background:linear-gradient(120deg,#e8e4e2,#2f7f7a 55%,#d9c3b7)" role="img" aria-label="Hands knitting teal yarn"></div><h3>KNITTING COURSES</h3><p>Lorem Ipsum is simply dummy text of the printing and typesetting industry. Lorem Ipsum is simply dummy text of the printing and typesetting industry.</p></article>
  <article class="abs activity" style="left:678px"><div class="activity-img" style="background:linear-gradient(120deg,#5d7bb0,#c9a88d 50%,#d96a5a)" role="img" aria-label="Children's hands doing crafts at a table"></div><h3>HANDCRAFTING COURSES</h3><p>Lorem Ipsum is simply dummy text of the printing and typesetting industry. Lorem Ipsum is simply dummy text of the printing and typesetting industry.</p></article>
</section>

<section class="voices">
  <h2 class="abs voices-title">What People <span>Say</span><br><span>About us</span></h2>
  <div class="abs voices-img" style="background:linear-gradient(135deg,#3f3a38,#b9b2a8 50%,#5a4f4a)" role="img" aria-label="Volunteers sorting food donations"></div>
  <svg class="abs arrow" style="left:551px" viewBox="0 0 34 34"><circle cx="17" cy="17" r="17" fill="#231f20"/><path d="M24 17H10m5-5-5 5 5 5" stroke="#fff" stroke-width="2" fill="none"/></svg>
  <svg class="abs arrow" style="left:610px" viewBox="0 0 34 34"><circle cx="17" cy="17" r="17" fill="#e0305a"/><path d="M10 17h14m-5-5 5 5-5 5" stroke="#fff" stroke-width="2" fill="none"/></svg>
  <div class="abs quote-card">
    <p>Lorem Ipsum is simply dummy text of the printing and typesetting industry. Lorem Ipsum is simply dummy text of the printing and typesetting industry.</p>
    <div class="stars">★★★★★</div>
    <div class="quote-name">Daniel K-</div>
    <div class="avatar" role="img" aria-label="Avatar of the reviewer"></div>
  </div>
</section>

<footer class="site-footer">
  <div class="abs footer-title">Nonprofit Women's Association</div>
  <div class="abs footer-rule" style="top:150px"></div>
  <nav class="abs footer-nav" style="top:143px;height:56px;align-items:center"><a>Home</a><a>Our Activities</a><a>Our Services</a><a>Terms &amp; Conditions</a><a>Privacy Policy</a></nav>
  <div class="abs footer-rule" style="top:206px"></div>
  <div class="abs copyright">Copyright 2023 | All Rights Reserved</div>
</footer>

</body>
</html>
```